Presentation Folder and Insert

We need design for a standard 9 x 12 presentation folder.

We need design for one template for a 8.5 x 11 insert/sales sheet(s) that will go inside the presentation folder.

See attached layout for presentation folder.

Left and Right flap on inside with slits on right flap for business card.

Would like design and colour schemes for both folder and insert template to flow with look of attached business card.

Target Market(s)

small business owners, marketing managers, media buyers and advertising agencies.

Industry/Entity Type

Business

Requirements
Must have
• Bright and colourful on front, back and inside.

Template for insert should flow with look of folder.

Insert will need room for us to add our own content.

```html
<!DOCTYPE html>
<html lang="en">
<head>
<meta charset="utf-8">
<title>Vantora Media – Presentation Folder</title>
<link href="https://fonts.googleapis.com/css2?family=Archivo:wght@800&display=swap" rel="stylesheet">
<style>
  :root {
    --page: #ffffff;
    --brand-blue: #0070bb;
    --brand-blue-deep: #0066b0;
    --brand-blue-soft: #0a78c2;
    --paper-light: #efefef;
    --mark-grey: #7a7a7a;
    --tagline-grey: #6b6b6b;
    --name-blue: #2a6db5;
    --name-white: #ffffff;
    --ghost: rgba(255, 255, 255, 0.07);
  }
  html, body {
    margin: 0;
    padding: 0;
    overflow: hidden;
    background: var(--page);
  }
  .canvas {
    position: relative;
    width: 1200px;
    height: 1000px;
    background: var(--page);
    overflow: hidden;
    font-family: "Archivo", "Arial Black", sans-serif;
  }
  .folder-art {
    position: absolute;
    inset: 0;
  }

  /* brand lockup: square + stacked name + tagline */
  .brand-lockup {
    position: absolute;
    top: 413px;
    width: 264px;
    height: 125px;
  }
  .brand-lockup--front { left: 209px; }
  .brand-lockup--inside { left: 733px; }
  .brand-square {
    position: absolute;
    left: 0;
    top: 0;
    width: 104px;
    height: 125px;
    border-radius: 18px;
    background: var(--mark-grey);
  }
  .brand-name {
    position: absolute;
    left: 109px;
    top: 18px;
    margin: 0;
    font-weight: 800;
    font-size: 36px;
    line-height: 38px;
    letter-spacing: -0.5px;
    white-space: nowrap;
  }
  .brand-tagline {
    position: absolute;
    left: 109px;
    top: 114px;
    margin: 0;
    font-weight: 800;
    font-size: 11.5px;
    line-height: 12px;
    letter-spacing: 0.6px;
    white-space: nowrap;
  }
  .brand-lockup--front .brand-name,
  .brand-lockup--front .brand-tagline { color: var(--name-white); }
  .brand-lockup--inside .brand-name { color: var(--name-blue); }
  .brand-lockup--inside .brand-tagline { color: var(--tagline-grey); }

  /* faint oversized name on the front cover */
  .panel-clip {
    position: absolute;
    left: 81px;
    top: 63px;
    width: 518px;
    height: 823px;
    overflow: hidden;
    pointer-events: none;
  }
  .ghost-name,
  .ghost-tagline {
    position: absolute;
    font-weight: 800;
    color: var(--ghost);
    white-space: nowrap;
    transform-origin: left center;
  }
  .ghost-name {
    left: 40px;
    top: 90px;
    font-size: 170px;
    line-height: 1;
    transform: rotate(40deg);
  }
  .ghost-tagline {
    left: 150px;
    top: 480px;
    font-size: 26px;
    letter-spacing: 2px;
    transform: rotate(38deg);
  }
</style>
</head>
<body>
  <div class="canvas">
    <svg class="folder-art" width="1200" height="1000" viewBox="0 0 1200 1000" aria-hidden="true">
      <!-- front cover -->
      <rect x="81" y="63" width="518" height="823" fill="var(--brand-blue)"/>
      <path d="M81 63 H340 C380 250 480 380 599 470 V63 Z" fill="var(--brand-blue-deep)"/>
      <path d="M81 700 C300 680 470 760 540 886 H81 Z" fill="var(--brand-blue-soft)"/>
      <!-- inside flap -->
      <rect x="599" y="63" width="516" height="823" fill="var(--paper-light)"/>
      <path d="M708 63 C730 280 900 400 1115 470 V63 Z" fill="var(--brand-blue)"/>
      <path d="M599 488 C850 580 1030 720 1068 886 H599 Z" fill="var(--brand-blue)"/>
      <path d="M599 700 C800 690 960 760 1060 886 H599 Z" fill="var(--brand-blue-deep)"/>
    </svg>

    <div class="panel-clip">
      <div class="ghost-name">Vantora</div>
      <div class="ghost-tagline">ADVERTISING NETWORK</div>
    </div>

    <div class="brand-lockup brand-lockup--front">
      <div class="brand-square"></div>
      <p class="brand-name">Vantora<br>Media</p>
      <p class="brand-tagline">ADVERTISING NETWORK</p>
    </div>

    <div class="brand-lockup brand-lockup--inside">
      <div class="brand-square"></div>
      <p class="brand-name">Vantora<br>Media</p>
      <p class="brand-tagline">ADVERTISING NETWORK</p>
    </div>
  </div>
</body>
</html>
```